Zielgruppe
Wir sind ein Handwerksunternehemen im Bereich Elektrotechnik.
Wir sind speziell im Neubau und bei Sanierungen im Einsatz. Eh
Es wird ein passender Flyer für potentielle Neukkunden benötigt.
Der Gewinner soll uns im Anschluss zwei weitere Flyer für andere Themenbereiche erstellen!
Aufgabenstellung
Wir wünschen uns einen professionellen Flyer.
Unsere Vorgaben können gerne kreativ geändert werden.
Stockbilder evtl. passend zum Neubau / Sanierung können verwendet werden.
Bitte die Druckvorlagen beachten von Satzhaus Nord
Im Anhang sind noch zwei Flyer von anderen Unternehmen. So in der Art stellen wir uns den Flyer vor.
Im Anhang:

```html
<!DOCTYPE html>
<html lang="de">
<head>
<meta charset="utf-8">
<title>Brandt &amp; Kessel Elektrotechnik – Flyer</title>
<link rel="stylesheet" href="https://fonts.googleapis.com/css2?family=Exo+2:wght@500;600;700&family=Arimo:wght@400;700&display=swap">
<style>
  :root {
    --blue: #1a96cf;
    --teal: #0b8a8f;
    --text: #555b60;
    --dark: #4a4f54;
    --white: #ffffff;
    --photo-warm: #d9cfc6;
    --photo-cool: #9fb7cc;
  }
  * { box-sizing: border-box; margin: 0; padding: 0; }
  html, body { width: 1200px; height: 822px; overflow: hidden; background: var(--white); }
  .flyer { position: relative; width: 1200px; height: 822px; background: var(--white); font-family: "Arimo", Arial, sans-serif; color: var(--text); overflow: hidden; }
  .abs { position: absolute; }

  .band { position: absolute; left: 0; width: 1200px; }
  .band-top { top: 0; height: 23px; }
  .band-bottom { top: 775px; height: 23px; }
  .band-label { position: absolute; top: 777px; font-family: "Exo 2", sans-serif; font-weight: 600; font-size: 17px; color: var(--white); letter-spacing: .6px; white-space: nowrap; }

  .heading { font-family: "Exo 2", sans-serif; font-weight: 600; color: var(--blue); letter-spacing: .6px; white-space: nowrap; }
  .heading-intro { left: 40px; top: 52px; font-size: 25px; line-height: 28px; }
  .heading-solution { left: 438px; top: 530px; font-size: 23px; }

  .copy { font-size: 13.6px; line-height: 19.6px; color: var(--text); white-space: nowrap; }
  .copy strong { color: var(--blue); font-weight: 700; }
  .problem-1 { left: 40px; top: 144px; }
  .problem-2 { left: 40px; top: 299px; }
  .problem-3 { left: 40px; top: 376px; }
  .problem-4 { right: 833px; top: 435px; text-align: right; }
  .solution-1 { left: 438px; top: 583px; }
  .solution-2 { left: 438px; top: 698px; }

  .brand { left: 840px; top: 68px; width: 300px; text-align: center; }
  .brand-mark { width: 100px; height: 100px; margin: 0 auto 14px; border-radius: 50%; background: var(--blue); }
  .brand-name { font-family: "Exo 2", sans-serif; font-weight: 700; font-size: 30px; color: var(--blue); letter-spacing: 1px; line-height: 32px; white-space: nowrap; }
  .brand-sub { display: flex; align-items: center; gap: 6px; font-family: "Exo 2", sans-serif; font-weight: 600; font-size: 12px; letter-spacing: 3px; color: var(--dark); }
  .brand-sub::before, .brand-sub::after { content: ""; flex: 1; height: 1px; background: var(--dark); }

  .contact { left: 849px; display: flex; gap: 18px; align-items: flex-start; font-size: 16px; line-height: 21px; color: var(--blue); white-space: nowrap; }
  .contact .icon { width: 36px; height: 36px; border-radius: 50%; background: var(--blue); flex: none; display: flex; align-items: center; justify-content: center; }
  .contact .label { padding-top: 8px; }
  .contact strong { font-weight: 700; }

  .cta { left: 801px; top: 527px; width: 367px; height: 65px; background: var(--blue); border-radius: 0 33px 33px 0; }
  .cta-text { position: absolute; left: 46px; top: 11px; font-family: "Exo 2", sans-serif; font-weight: 700; font-size: 18px; line-height: 22px; color: var(--white); letter-spacing: .6px; white-space: nowrap; }
  .cta svg { position: absolute; right: 24px; top: 8px; }

  .social { left: 849px; display: flex; align-items: center; gap: 18px; font-size: 13.6px; line-height: 17px; color: var(--dark); white-space: nowrap; }
  .social .dot { width: 38px; height: 38px; border-radius: 50%; flex: none; }

  .calendar-badge { left: 660px; top: 380px; width: 112px; height: 112px; border-radius: 50%; background: var(--teal); border: 4px solid var(--white); display: flex; align-items: center; justify-content: center; }
  .mini-brand { left: 591px; top: 424px; width: 80px; height: 80px; border-radius: 50%; background: var(--blue); border: 4px solid var(--white); display: flex; align-items: center; justify-content: center; font-family: "Exo 2", sans-serif; font-weight: 700; font-size: 20px; color: var(--white); }
</style>
</head>
<body>
<main class="flyer">

  <svg class="band band-top" width="1200" height="23" viewBox="0 0 1200 23">
    <rect width="1200" height="23" fill="var(--teal)"/>
    <polygon points="0,0 835,0 877,23 0,23" fill="var(--blue)"/>
    <polygon points="835,0 855,0 897,23 877,23" fill="var(--white)"/>
  </svg>

  <svg class="abs" style="left:298px;top:23px" width="502" height="372" viewBox="0 0 502 372" role="img" aria-label="Foto: lachende Familie sitzt im neuen Zuhause auf dem Boden und formt mit den Armen ein Dach">
    <defs>
      <clipPath id="family-clip"><circle cx="340" cy="63" r="318"/></clipPath>
      <linearGradient id="family-tone" x1="0" y1="0" x2="1" y2="1">
        <stop offset="0" stop-color="var(--photo-warm)"/>
        <stop offset="1" stop-color="var(--photo-cool)"/>
      </linearGradient>
    </defs>
    <rect width="502" height="372" fill="url(#family-tone)" clip-path="url(#family-clip)"/>
  </svg>

  <svg class="abs" style="left:192px;top:78px" width="200" height="200" viewBox="0 0 200 200" role="img" aria-label="Foto: Steckdose, Werkzeug und Bauplan auf dem Tisch">
    <circle cx="100" cy="100" r="96" fill="#c9ccd0" stroke="var(--white)" stroke-width="6"/>
  </svg>

  <svg class="abs" style="left:0;top:474px" width="305" height="301" viewBox="0 0 305 301" role="img" aria-label="Foto: lächelnder Elektriker in Arbeitskleidung verlegt Kabel an der Wand">
    <defs><linearGradient id="worker-tone" x1="0" y1="0" x2="0" y2="1">
      <stop offset="0" stop-color="#cfd2d4"/><stop offset="1" stop-color="#6f8fb0"/>
    </linearGradient></defs>
    <circle cx="150" cy="152" r="152" fill="url(#worker-tone)"/>
  </svg>

  <h2 class="abs heading heading-intro">Sie kennen es<br>bestimmt...</h2>
  <p class="abs copy problem-1">Viele Handwerks-<br>betriebe setzen auf<br>der Baustelle zu<br><strong>wenig qualifizierte<br>Mitarbeiter</strong> ein,<br>wodurch es in der Praxis<br>oft zu Mängeln kommt.</p>
  <p class="abs copy problem-2"><strong>Schlechte Kommunikation</strong> auf der Baustelle<br>oder sogar mit den Unternehmen führen schnell<br>zu Missverständnissen.</p>
  <p class="abs copy problem-3">Durch eine <strong>schlechte Beratung oder Planung</strong><br>kommt es zu Nachträgen und Verzögerungen.</p>
  <p class="abs copy problem-4">Diese Probleme führen in den meisten Fällen<br>zu einer Bauverzögerung<br>und Mehrkosten.</p>

  <div class="abs calendar-badge">
    <svg width="62" height="62" viewBox="0 0 62 62" fill="none" stroke="var(--white)" stroke-width="3.5">
      <rect x="4" y="9" width="44" height="40" rx="4"/><line x1="4" y1="19" x2="48" y2="19"/>
      <line x1="15" y1="4" x2="15" y2="13"/><line x1="37" y1="4" x2="37" y2="13"/>
      <path d="M12 27h4M22 27h4M32 27h4M12 35h4M22 35h4M12 42h4"/>
      <circle cx="46" cy="46" r="12" fill="var(--teal)"/><path d="M40 46l4 4 8-8"/>
    </svg>
  </div>
  <div class="abs mini-brand">B&amp;K</div>

  <h2 class="abs heading heading-solution">Unsere Lösung</h2>
  <p class="abs copy solution-1">Uns ist wichtig, dass Bauherren pünktlich in ihr<br>neues Zuhause einziehen können mit maximaler<br>Zufriedenheit an der handwerklichen Ausführung<br>damit unsere Kunden immer zufriedene<br>Auftraggeber haben.</p>
  <p class="abs copy solution-2">Um diesem Anspruch gerecht zu werden, setzen<br>wir nur auf eigene ausgebildete Fachkräfte.</p>

  <div class="abs brand">
    <div class="brand-mark"></div>
    <div class="brand-name">BRANDT &amp; KESSEL</div>
    <div class="brand-sub">ELEKTROTECHNIK</div>
  </div>

  <div class="abs contact" style="top:278px">
    <span class="icon"><svg width="18" height="20" viewBox="0 0 18 20" fill="none" stroke="var(--white)" stroke-width="2"><path d="M9 19s-6-6-6-11a6 6 0 0 1 12 0c0 5-6 11-6 11z"/><circle cx="9" cy="8" r="2"/></svg></span>
    <div class="label" style="padding-top:0"><strong>Brandt &amp; Kessel Elektrotechnik<br>GmbH &amp; Co.KG</strong><br><span style="display:block;height:10px"></span>Lindenweg 14<br>22880 Wedel</div>
  </div>
  <div class="abs contact" style="top:382px">
    <span class="icon"><svg width="18" height="18" viewBox="0 0 24 24" fill="var(--white)"><path d="M6.6 10.8a15 15 0 0 0 6.6 6.6l2.2-2.2a1 1 0 0 1 1-.25 11.4 11.4 0 0 0 3.6.6 1 1 0 0 1 1 1V20a1 1 0 0 1-1 1A17 17 0 0 1 3 4a1 1 0 0 1 1-1h3.5a1 1 0 0 1 1 1c0 1.25.2 2.45.6 3.6a1 1 0 0 1-.25 1z"/></svg></span>
    <div class="label">040 31 47 82 90</div>
  </div>
  <div class="abs contact" style="top:424px">
    <span class="icon"><svg width="18" height="16" viewBox="0 0 18 16" fill="none" stroke="var(--white)" stroke-width="1.8"><path d="M1 6l8-5 8 5v9H1z"/><path d="M1 6l8 5 8-5"/></svg></span>
    <div class="label">info@brandt-kessel.de</div>
  </div>
  <div class="abs contact" style="top:465px">
    <span class="icon"><svg width="20" height="20" viewBox="0 0 20 20" fill="none" stroke="var(--white)" stroke-width="1.6"><circle cx="10" cy="10" r="8"/><ellipse cx="10" cy="10" rx="3.5" ry="8"/><line x1="2" y1="10" x2="18" y2="10"/></svg></span>
    <div class="label">www.brandt-kessel.de</div>
  </div>

  <div class="abs cta">
    <div class="cta-text">VEREINBAREN SIE<br>JETZT EINEN TERMIN.</div>
    <svg width="50" height="50" viewBox="0 0 62 62" fill="none" stroke="var(--white)" stroke-width="3.5">
      <rect x="4" y="9" width="44" height="40" rx="4"/><line x1="4" y1="19" x2="48" y2="19"/>
      <line x1="15" y1="4" x2="15" y2="13"/><line x1="37" y1="4" x2="37" y2="13"/>
      <path d="M12 27h4M22 27h4M32 27h4M12 35h4M22 35h4M12 42h4"/>
      <circle cx="46" cy="46" r="12" fill="var(--blue)"/><path d="M40 46l4 4 8-8"/>
    </svg>
  </div>

  <div class="abs social" style="top:642px">
    <span class="dot" style="background:var(--blue)"></span>
    <span>www.netzwerk-eins.de/<br>brandtkesselelektrotechnik</span>
  </div>
  <div class="abs social" style="top:698px">
    <span class="dot" style="background:var(--teal)"></span>
    <span>www.bildkanal.de/<br>brandt_kessel_elektrotechnik</span>
  </div>

  <svg class="band band-bottom" width="1200" height="23" viewBox="0 0 1200 23">
    <rect width="1200" height="23" fill="var(--teal)"/>
    <polygon points="0,0 445,0 386,23 0,23" fill="var(--blue)"/>
    <polygon points="445,0 467,0 408,23 386,23" fill="var(--white)"/>
  </svg>
  <span class="band-label" style="left:40px">info@brandt-kessel.de</span>
  <span class="band-label" style="right:32px">www.brandt-kessel.de</span>

</main>
</body>
</html>
```